brightlakePRESS is publishing a new book and needs some exceptional cover and layout design!

We are publishing a narrow niche PDF eBook and need both a great cover AND great magazine style layout.

The eBook is a compilation of interviews with 12 financial experts on a particular topic. So the format is is the same for each interview 'chapter'

We are looking for a good front cover/document design that will make what is a pretty dry topic, exciting, interesting and easy to read. Basically - magazine style layout.

The specs for the front cover are:

Title:

The Hurdles and Openings Before Bookkeepers and Planners In Expanding Their Pension Fund Practice In 2014 -2015

by Tom Vellani

published by brightlakePRESS

The client would like a similar cover to the one I have attached for your reference. (book front cover example). By no means be limited by this design suggestion. The only caveat is that shots of all interview subjects are included (except the author). These have been included in the zip file.

The design for the text should be elegant and consistent with the design of the front cover. Please format the text in pages 1 to 15 to demonstrate you've understood the brief.

Attached files.

1) MS word version of draft book pages 1 to 15
2) copy of the cover my client would like to emulate.

reminder - this is destined to be a PDF eBook - so looking for some nice eye catching magazine style layout in the design. Columns would be fine.

Good luck!

Brent Marlow
brightlakePRESS

Target Market(s)

Professional Accountants who are running there own businesses

Industry/Entity Type

Financial

Colors

Designer to choose colors to be used in the design.

Requirements
Must have
• The cover must feature headshots of all the interview subjects. The PDF layout must be optimised for viewing on an iPad

```html
<!DOCTYPE html>
<html lang="en">
<head>
<meta charset="utf-8">
<title>The Hurdles and Openings – Tom Vellani</title>
<link rel="stylesheet" href="https://fonts.googleapis.com/css2?family=Oranienbaum&family=Arimo&family=Questrial&display=swap">
<style>
  :root {
    --navy: #1a5f9c;
    --band-blue: #1469b3;
    --title-orange: #ee5a2a;
    --title-blue: #1970b8;
    --title-grey: #6b6b6b;
    --subtitle-red: #d8262f;
    --paper: #ffffff;
  }
  * { margin: 0; padding: 0; box-sizing: border-box; }
  html, body { width: 800px; height: 1200px; overflow: hidden; background: var(--paper); }
  .cover {
    position: relative;
    width: 800px;
    height: 1200px;
    background: var(--paper);
    overflow: hidden;
  }
  .top-rule {
    position: absolute; top: 0; left: 0;
    width: 100%; height: 15px;
    background: var(--navy);
  }
  .title {
    position: absolute; top: 0; left: 0; width: 100%; height: 570px;
    font-family: "Oranienbaum", "Times New Roman", serif;
    font-weight: 400;
  }
  .title span {
    position: absolute; left: 0; width: 100%;
    text-align: center;
    line-height: 1;
    white-space: nowrap;
  }
  .title-the { top: 58px; font-size: 100px; color: var(--title-grey); }
  .title-main { top: 140px; font-size: 200px; color: var(--title-orange); letter-spacing: -1px; }
  .title-and { top: 316px; font-size: 86px; color: var(--title-grey); }
  .title-second { top: 392px; font-size: 146px; color: var(--title-blue); letter-spacing: -1px; }
  .subtitle {
    position: absolute; top: 584px; left: 0; width: 100%;
    text-align: center;
    font-family: "Arimo", Arial, sans-serif;
    font-size: 30px;
    line-height: 50px;
    color: var(--subtitle-red);
  }
  .contributors {
    position: absolute; top: 752px; left: 0;
    width: 800px; height: 253px;
    display: grid;
    grid-template-columns: repeat(8, 1fr);
    grid-template-rows: repeat(2, 1fr);
    gap: 2px;
  }
  .headshot { display: block; width: 100%; height: 100%; }
  .author-band {
    position: absolute; top: 1005px; left: 0;
    width: 100%; height: 195px;
    background: var(--band-blue);
    display: flex; align-items: center; justify-content: center;
  }
  .author-name {
    font-family: "Questrial", "Century Gothic", sans-serif;
    font-size: 76px;
    color: var(--paper);
    letter-spacing: 1px;
  }
</style>
</head>
<body>
  <main class="cover">
    <div class="top-rule"></div>

    <h1 class="title">
      <span class="title-the">The</span>
      <span class="title-main">Hurdles</span>
      <span class="title-and">and</span>
      <span class="title-second">Openings</span>
    </h1>

    <p class="subtitle">
      Before Bookkeepers and Planners<br>
      In Expanding Their Pension Fund Practice In<br>
      2014 -2015
    </p>

    <section class="contributors" aria-label="Interview subjects">
      <svg class="headshot" role="img" aria-label="Headshot of interview subject 1"><rect width="100%" height="100%" fill="#8e8f92"/></svg>
      <svg class="headshot" role="img" aria-label="Headshot of interview subject 2"><rect width="100%" height="100%" fill="#6f6a66"/></svg>
      <svg class="headshot" role="img" aria-label="Headshot of interview subject 3"><rect width="100%" height="100%" fill="#d9c7b4"/></svg>
      <svg class="headshot" role="img" aria-label="Headshot of interview subject 4"><rect width="100%" height="100%" fill="#c9c6c1"/></svg>
      <svg class="headshot" role="img" aria-label="Headshot of interview subject 5"><rect width="100%" height="100%" fill="#a9b6c2"/></svg>
      <svg class="headshot" role="img" aria-label="Headshot of interview subject 6"><rect width="100%" height="100%" fill="#8a8c8e"/></svg>
      <svg class="headshot" role="img" aria-label="Headshot of interview subject 7"><rect width="100%" height="100%" fill="#c28f6e"/></svg>
      <svg class="headshot" role="img" aria-label="Headshot of interview subject 8"><rect width="100%" height="100%" fill="#7f9a6c"/></svg>
      <svg class="headshot" role="img" aria-label="Headshot of interview subject 9"><rect width="100%" height="100%" fill="#c9a58a"/></svg>
      <svg class="headshot" role="img" aria-label="Headshot of interview subject 10"><rect width="100%" height="100%" fill="#b5a89a"/></svg>
      <svg class="headshot" role="img" aria-label="Headshot of interview subject 11"><rect width="100%" height="100%" fill="#9c8f85"/></svg>
      <svg class="headshot" role="img" aria-label="Headshot of interview subject 12"><rect width="100%" height="100%" fill="#5e6670"/></svg>
      <svg class="headshot" role="img" aria-label="Headshot of interview subject 13"><rect width="100%" height="100%" fill="#9aa7b5"/></svg>
      <svg class="headshot" role="img" aria-label="Headshot of interview subject 14"><rect width="100%" height="100%" fill="#7d7470"/></svg>
      <svg class="headshot" role="img" aria-label="Headshot of interview subject 15"><rect width="100%" height="100%" fill="#a8b0b8"/></svg>
      <svg class="headshot" role="img" aria-label="Headshot of interview subject 16"><rect width="100%" height="100%" fill="#b08a6e"/></svg>
    </section>

    <footer class="author-band">
      <p class="author-name">Tom Vellani</p>
    </footer>
  </main>
</body>
</html>
```